Business Cards & Stationery for a Gold Refiner
Brambleton Assets
Business Cards & Stationery for a Gold Refiner - Jewelry
Creative Brief
Professional
(MUST BE LEFT BLANK)
18 East 52nd Street, Lobby Rear, New York, NY 10022
(212)-584-MINT (6468)
info@brambletonassetsllc.example
Hey Designers, We would like for our telephone, fax, and email to be titled with symbols instead of words, e.g. a small telephone symbol next to the phone number and a fax machine next to the fax number. We require blank fields we can fill in, with no symbols, for: NAME, TITLE We require blank fields we can fill in, with symbols, for: CELL NUMBER, EMAIL, WEB ADDRESS Also, and this point is VERY IMPORTANT, we need the final deliverables to include an editable Adobe Illustrator and/or Photoshop file (preferably, Illustrator). We will include the names and titles of our individual employees ourselves, thus we need those sections to be left blank. All fields should be editable. We will not accept the design if it does not include a fully editable file. Our logo was recently completed and we require it to be included in the design. The file should be attached to the contest. We have additional versions of the logo we'd like to be able to swap out at will, however they are all in the same style as the logo provided, so the color scheme of the logo should be utilized throughout. The font should be traditional and corporate in style, and not too stylized or flashy. The logo should be included on the back as well. Thanks Everybody and Good Luck!

```html
<!DOCTYPE html>
<html lang="en">
<head>
<meta charset="utf-8">
<title>Brambleton Assets – Business Card</title>
<link rel="stylesheet" href="https://fonts.googleapis.com/css2?family=Oswald:wght@600&family=Open+Sans:wght@400;600;700&display=swap">
<style>
  :root {
    --gold: #d4a216;
    --gold-dark: #b88a0c;
    --gold-shade: #c39413;
    --ink: #6b6b6d;
    --paper: #ffffff;
    --backdrop: #e8e7e4;
  }
  * { margin: 0; padding: 0; box-sizing: border-box; }
  html, body { width: 1200px; height: 799px; overflow: hidden; }
  body {
    background: var(--backdrop);
    font-family: "Open Sans", Arial, sans-serif;
    position: relative;
  }
  .card {
    position: absolute;
    top: 235px;
    width: 520px;
    height: 320px;
    border-radius: 28px;
    overflow: hidden;
    box-shadow: 0 10px 24px rgba(0,0,0,0.18);
  }
  .card-back { left: 60px; background: var(--gold); }
  .card-front { left: 620px; background: var(--paper); }

  .side-shapes { position: absolute; inset: 0; }

  .brand {
    display: flex;
    align-items: center;
    gap: 10px;
  }
  .brand-square { width: 44px; height: 44px; flex: none; }
  .brand-name {
    font-family: "Oswald", "Arial Narrow", sans-serif;
    font-weight: 600;
    text-transform: uppercase;
    line-height: 0.95;
    letter-spacing: 0.5px;
  }

  .card-back .brand {
    position: absolute;
    left: 50%;
    top: 108px;
    transform: translateX(-50%);
  }
  .card-back .brand-square { background: var(--paper); }
  .card-back .brand-name { color: var(--paper); font-size: 30px; }
  .back-url {
    position: absolute;
    left: 0; right: 0;
    top: 206px;
    text-align: center;
    color: var(--paper);
    font-size: 12px;
    font-weight: 600;
  }

  .holder { position: absolute; left: 44px; top: 30px; }
  .holder-name { color: var(--gold); font-size: 19px; font-weight: 700; }
  .holder-title { color: var(--ink); font-size: 11px; margin-top: 1px; }

  .contact-list {
    position: absolute;
    left: 44px;
    top: 118px;
    list-style: none;
  }
  .contact-list li {
    display: flex;
    align-items: center;
    gap: 8px;
    color: var(--ink);
    font-size: 11.5px;
    line-height: 16px;
  }
  .contact-dot {
    width: 9px; height: 9px;
    border-radius: 50%;
    background: var(--gold);
    flex: none;
  }

  .card-front .brand { position: absolute; left: 298px; top: 120px; }
  .card-front .brand-square { background: var(--gold); }
  .card-front .brand-name { color: var(--ink); font-size: 27px; }

  .front-wave { position: absolute; left: 0; bottom: 0; width: 520px; height: 120px; }
</style>
</head>
<body>

  <section class="card card-back" aria-label="Card back">
    <svg class="side-shapes" viewBox="0 0 520 320" aria-hidden="true">
      <polygon points="40,50 115,50 155,160 115,270 40,270" fill="var(--gold-shade)"/>
      <polygon points="480,50 405,50 365,160 405,270 480,270" fill="var(--gold-shade)"/>
    </svg>
    <div class="brand">
      <span class="brand-square"></span>
      <span class="brand-name">Brambleton<br>Assets</span>
    </div>
    <p class="back-url">www.brambletonassetsllc.example</p>
  </section>

  <section class="card card-front" aria-label="Card front">
    <div class="holder">
      <p class="holder-name">Mara Ellison</p>
      <p class="holder-title">President</p>
    </div>
    <ul class="contact-list">
      <li><span class="contact-dot"></span>(212)-584-MINT (6468)</li>
      <li><span class="contact-dot"></span>555.010.2233</li>
      <li><span class="contact-dot"></span>(212)-584-6470</li>
      <li><span class="contact-dot"></span>info@brambletonassetsllc.example</li>
      <li><span class="contact-dot"></span>www.brambletonassetsllc.example</li>
    </ul>
    <div class="brand">
      <span class="brand-square"></span>
      <span class="brand-name">Brambleton<br>Assets</span>
    </div>
    <svg class="front-wave" viewBox="0 0 520 120" preserveAspectRatio="none" aria-hidden="true">
      <path d="M0,40 C140,110 320,30 520,62" fill="none" stroke="var(--gold)" stroke-width="2"/>
      <path d="M0,68 C150,128 330,52 520,80 L520,120 L0,120 Z" fill="var(--gold)"/>
      <path d="M0,92 C160,130 340,78 520,98" fill="none" stroke="var(--gold-dark)" stroke-width="1.5" opacity="0.6"/>
    </svg>
  </section>

</body>
</html>
```